Property lawyer needs a website for new law firm Sydney

WHO AM I ?
I am a real estate development lawyer based in suburban Sydney Australia with over 14 years experience and have recently started my own law firm "Tallowbrook Legal". The firm is just me (a female) at this stage. I need a website designed that is capable of being edited by me frequently (hoping this is easily done?!) and can be published with the domain name I own - www.tallowbrooklegal.com.au.
My areas of practice are:
* Property development (strata & community titling, due diligence, easements, by-laws and management statements, structuring etc)
* Conveyancing (sale and purchase of residential, commercial and retail property)
* General property law (caveats, transfers, related party transactions, easements, leases, powers of attorney etc).
WEBSITE REQUIREMENTS
I would like a website which conveys professionalism, has a fresh modern corporate look and is easy to navigate. The website will mostly be accessed by potential clients looking for information about me, my areas of practice and how to get in contact with me. My potential clients are corporate developers and individuals who are buying and selling property.
My logo for Tallowbrook Legal (see attached) is simple, clean and professional looking. I would like the website to work with the logo without being too dark.
I haven't written all of the content yet, so please use filler text for everything and structure the menus as described above. The site will need to be capable of being updated and edited by me.
Other than that I will leave the design up to you.
Thanks and happy designing!
Target Market(s)
Professional developers and individuals buying and selling real estate
Industry/Entity Type
Real Estate
Coding
Coded - Design and coding required
Number of Pages Required
4 page
Requirements
Must have
- I would like a website which conveys professionalism, has a fresh modern corporate look and is easy to navigate. The website will mostly be accessed by potential clients looking for information about me, my areas of practice and how to get in contact with me. My potential clients are corporate developers and individuals who are buying and selling property.
- Please use my logo for Tallowbrook Legal. I would like the website to work with the logo - the colours are a dark blue (C 100% M 50% B 50%) and grey (C10% B 40%). I don't want the website to be too dark though.
- I am thinking 4 pages. I would like links across the top of the page for "Practice Areas", "About us" and "Contact us" - these should lead to separate landing pages with the content to be inserted later.
- The contact page should contain space for a potential client to send an email enquiry to the following email address "enquiries@tallowbrooklegal.com.au". My contact details are set out in the attached letterhead (see attached).
- I would also like the home page to set out what my three Practice Areas are - Property Development; Conveyancing; General Property Law. Each area should have some filler text under it which will be completed later and a link to be able to take me to the "Practice Areas" page where more detail on each will be provided.
- Please select images that are relevant to my practice as a property lawyer. The photos you use will be the ones which I use so please choose wisely.
- I will need a link on the bottom of the home page showing that I am a member of "The Counsel Guild of NSW" (see attached logo).
- The bottom of each page should also include the following statement "Tallowbrook Legal is a business name of Tallowbrook Legal Pty Limited ACN 482 517 306, an incorporated legal practice regulated by the Legal Profession Act 2004. Liability limited by a scheme approved under the Professional Standards Legislation."
Nice to have
- Have attached an image of me (not the best) but at least its me. Consider whether to use on "About us" page
Should not have
- No images of gavels, scales of justice or law books.
- Images not to be too masculine
- Website not to be too dark

```html
<!DOCTYPE html>
<html lang="en">
<head>
<meta charset="utf-8">
<title>Tallowbrook Legal</title>
<link rel="stylesheet" href="https://fonts.googleapis.com/css2?family=Roboto:wght@400;500;700&family=Oswald:wght@400&display=swap">
<style>
:root{
  --navy:#0b3a66;
  --navy-mid:#1d5a94;
  --text:#555;
  --footer-bg:#f1f1f1;
  --base-bg:#2c2c2c;
  --white:#fff;
}
*{box-sizing:border-box;margin:0;padding:0}
html,body{width:938px;height:1200px;overflow:hidden}
body{position:relative;background:var(--white);font-family:'Roboto',sans-serif;color:var(--text)}
.abs{position:absolute}
.topbar{left:0;top:0;width:938px;height:33px;background:var(--navy);color:var(--white);font-size:12px}
.topbar .email{left:68px;top:9px;display:flex;align-items:center;gap:5px}
.topbar .phones{right:68px;top:9px;display:flex;align-items:center;gap:5px}
.header{left:0;top:33px;width:938px;height:77px}
.brand{left:68px;top:27px;font-size:22px;font-weight:500;letter-spacing:.5px;color:var(--navy)}
.nav{right:68px;top:33px;display:flex;gap:32px;font-size:12px;color:#333;letter-spacing:.2px}
.nav .active{color:var(--navy-mid)}
.hero{left:0;top:110px;width:938px;height:434px;
  background:
    radial-gradient(ellipse 220px 200px at 300px 170px,rgba(255,255,255,.35),rgba(255,255,255,0) 70%),
    radial-gradient(ellipse 260px 70px at 780px 180px,rgba(235,238,242,.7),rgba(235,238,242,0) 70%),
    linear-gradient(180deg,#3d86cf 0%,#7fb6e2 28%,#b6d4e6 38%,#5f7e45 46%,#6a9a3a 58%,#5d942c 78%,#4c8323 100%)}
.hero-arrow{top:186px;width:32px;height:32px}
.hero-title{right:75px;top:255px;font-family:'Oswald',sans-serif;font-size:41px;color:var(--white);text-shadow:0 2px 4px rgba(0,0,0,.35);letter-spacing:-.5px}
.shadow-line{left:120px;top:544px;width:700px;height:22px;background:radial-gradient(ellipse at top,rgba(0,0,0,.12),rgba(0,0,0,0) 70%)}
.services-title{left:0;top:572px;width:938px;text-align:center;font-size:19px;font-weight:500;color:#333}
.services-title span{color:var(--navy)}
.service{top:614px;width:248px}
.service .photo{width:246px;height:154px;border:3px solid var(--white);box-shadow:0 0 3px rgba(0,0,0,.3)}
.service h3{margin-top:22px;font-size:14px;font-weight:400;color:var(--navy)}
.service p{margin-top:11px;font-size:10px;line-height:16px;color:var(--text)}
.btn{display:inline-block;margin-top:13px;width:82px;height:26px;line-height:26px;text-align:center;font-size:10px;font-weight:500;color:var(--white);background:linear-gradient(#2f7cc4,#17548f);border-radius:2px;box-shadow:0 1px 2px rgba(0,0,0,.4)}
.footer{left:0;top:924px;width:938px;height:166px;background:var(--footer-bg);border-top:1px solid #e3e3e3}
.legal-note{left:70px;top:42px;width:312px;font-size:10px;line-height:18.5px;color:#333}
.fcol{top:42px;font-size:10.3px;color:#444}
.fcol h4{font-size:11px;font-weight:500;color:var(--navy);margin-bottom:11px}
.fcol li{list-style:none;line-height:22px}
.base{left:0;top:1090px;width:938px;height:110px;background:var(--base-bg);color:var(--white)}
.base .links{left:70px;top:37px;font-size:10.3px}
.base .copy{left:70px;top:59px;font-size:12px}
.badge{left:619px;top:40px;width:92px;height:34px;background:#4a4a4a;border-radius:3px}
.socials{left:738px;top:42px;display:flex;gap:10px}
.socials span{display:block;width:27px;height:27px;border-radius:2px}
</style>
</head>
<body>
<div class="abs topbar">
  <div class="abs email">
    <svg width="12" height="9" viewBox="0 0 12 9"><rect x="0.5" y="0.5" width="11" height="8" fill="none" stroke="#fff"/><path d="M0.5 0.5L6 5L11.5 0.5" fill="none" stroke="#fff"/></svg>
    jhale@tallowbrooklegal.com.au
  </div>
  <div class="abs phones">
    <svg width="11" height="11" viewBox="0 0 11 11"><rect width="11" height="11" rx="2" fill="#fff"/><path d="M3 2.5c0 3 2.5 6 5.5 6l.5-1.5-1.5-1-1 .7c-1-.5-1.7-1.2-2.2-2.2l.7-1-1-1.5z" fill="#0b3a66"/></svg>
    02 9400 2618 &nbsp;|&nbsp;
    <svg width="7" height="11" viewBox="0 0 7 11"><rect x="0.5" y="0.5" width="6" height="10" rx="1" fill="none" stroke="#fff"/></svg>
    0400 735 912
  </div>
</div>

<header class="abs header">
  <div class="abs brand">TALLOWBROOK LEGAL</div>
  <nav class="abs nav">
    <span class="active">HOME</span><span>ABOUT US</span><span>PRACTISE AREAS</span><span>CONTACT US</span>
  </nav>
</header>

<section class="abs hero" role="img" aria-label="Photo of a green meadow under a blue sky with snowy mountains on the right, with a glowing white outline drawing of a house on the left">
  <svg class="abs hero-arrow" style="left:33px" viewBox="0 0 32 32"><circle cx="16" cy="16" r="14" fill="none" stroke="#fff" stroke-width="2.5"/><path d="M18 10l-6 6 6 6" fill="none" stroke="#fff" stroke-width="3"/></svg>
  <svg class="abs hero-arrow" style="left:872px" viewBox="0 0 32 32"><circle cx="16" cy="16" r="14" fill="none" stroke="#fff" stroke-width="2.5"/><path d="M14 10l6 6-6 6" fill="none" stroke="#fff" stroke-width="3"/></svg>
  <div class="abs hero-title">TALLOWBROOK LEGAL</div>
</section>
<div class="abs shadow-line"></div>

<h2 class="abs services-title">OUR <span>SERVICES</span></h2>

<article class="abs service" style="left:70px">
  <div class="photo" role="img" aria-label="Photo of a hand holding a small model house" style="background:linear-gradient(120deg,#e9f3d8,#9ccb6e 55%,#5e9e35)"></div>
  <h3>PROPERTY DEVELOPMENT</h3>
  <p>strata &amp; community titling, due diligence, easements, by-laws and management statements, structuring</p>
  <a class="btn">LEARN MORE</a>
</article>

<article class="abs service" style="left:345px">
  <div class="photo" role="img" aria-label="Photo of glass office towers against a blue sky" style="background:linear-gradient(90deg,#1f4f9c,#7fb0e0 50%,#2a4e80)"></div>
  <h3>CONVEYANCING</h3>
  <p>sale and purchase of residential, commercial and retail property</p>
  <a class="btn">LEARN MORE</a>
</article>

<article class="abs service" style="left:622px">
  <div class="photo" role="img" aria-label="Photo of house keys being handed over from one hand to another" style="background:linear-gradient(90deg,#b8c45a,#e8e4b8 50%,#c98a78)"></div>
  <h3>GENERAL PROPERTY LAW</h3>
  <p>caveats, transfers, related party transactions, easements, leases, powers of attorney</p>
  <a class="btn">LEARN MORE</a>
</article>

<footer class="abs footer">
  <p class="abs legal-note">Tallowbrook Legal is a business name of Tallowbrook Legal Pty Limited ACN 482 517 306, an incorporated legal practice regulated by the Legal Profession Act 2004. Liability limited by a scheme approved under the Professional Standards Legislation</p>
  <div class="abs fcol" style="left:427px"><h4>SPECIALISTS</h4><ul><li>Commercial</li><li>Residential</li><li>Luxury</li></ul></div>
  <div class="abs fcol" style="left:561px"><h4>AGENCIES</h4><ul><li>Sign Up</li><li>Forums</li><li>Promotions</li></ul></div>
  <div class="abs fcol" style="left:674px"><h4>CONTACT US</h4><ul><li>14 Wattle Lane, Hornsby NSW 2077</li><li>Phone: +61 2 9400 2600</li><li>E-mail: mail@tallowbrooklegal.com.au</li></ul></div>
</footer>

<div class="abs base">
  <div class="abs links">About &nbsp;|&nbsp; Disclaimer &nbsp;|&nbsp; Contact &nbsp;|&nbsp; Sitemap &nbsp;|&nbsp; Hosted Solutions Partner</div>
  <div class="abs copy">Copyright © 2015 &nbsp;All Rights</div>
  <div class="abs badge" role="img" aria-label="Member of The Counsel Guild of NSW badge"></div>
  <div class="abs socials">
    <span style="background:#2aa3de" role="img" aria-label="Social profile link"></span>
    <span style="background:#c4302b" role="img" aria-label="Video channel link"></span>
    <span style="background:#3b5998" role="img" aria-label="Social page link"></span>
    <span style="background:#0a77b5" role="img" aria-label="Professional network link"></span>
  </div>
</div>
</body>
</html>
```